Tov Fest Falcons

We are party planning business. We are a team of established individuals and business in party stream businesses like DJ, Caterers, Party supplies, Kids parties, Events & Private Parties and much more. So basically me and business collaborate a team of business or individuals to do clients party in the best way possible.

Target Market(s)

majority of them 16 to 30 -60% to 70 % and 30 to 40 year olds- 30% to 40 %

Industry/Entity Type

Party Planning

Contact Information for Business Card

Tov
Owner & Manager
0481927354
tovfestfalcons@mailbright.example

Requirements
Must have
• front side : Logo and list of services we provide
DJ's, Catering,All party supplies, Tinyvolta and more...just to show what the business is about when anyone looks at the card and at the rear side my details which are already provided.
Should not have
• Dont make it look we do kids party which is just one of the things we do but don't make my business card look like kids party specialist make it more connecting to youngsters and older crowd more

```html
<!DOCTYPE html>
<html lang="en">
<head>
<meta charset="utf-8">
<title>Tov Fest Falcons – Business Cards</title>
<link rel="stylesheet" href="https://fonts.googleapis.com/css2?family=Cormorant+Garamond:ital,wght@1,600;1,700&display=swap">
<style>
  :root {
    --page-bg: #e2c4b1;
    --ink: #111111;
    --glow: rgba(255,255,255,0.95);
    --brand-red: #c8161d;
    --art-balloon: #8e4a36;
    --art-spark: #6f7a3a;
    --art-cake: #9a9a9a;
    --metal: linear-gradient(112deg,
      #101010 0%, #5a5a5a 14%, #f4f4f4 32%, #8a8a8a 44%,
      #0c0c0c 56%, #bdbdbd 66%, #f7f7f7 73%, #3a3a3a 86%, #0e0e0e 100%);
  }
  * { box-sizing: border-box; margin: 0; padding: 0; }
  html, body { width: 1200px; height: 1000px; overflow: hidden; }
  body {
    background: var(--page-bg);
    font-family: "Cormorant Garamond", Georgia, serif;
    font-style: italic;
    color: var(--ink);
    position: relative;
  }
  .card {
    position: absolute;
    width: 560px;
    height: 340px;
    background: var(--metal);
    overflow: hidden;
  }
  .card--front { left: 120px; top: 110px; }
  .card--back  { left: 520px; top: 550px; }

  .glow-text {
    font-weight: 600;
    text-shadow: 0 0 8px var(--glow), 0 0 4px var(--glow), 0 0 2px var(--glow);
  }

  /* illustration placeholders: plain soft-gradient panels */
  .art { position: absolute; border-radius: 6px; opacity: 0.55; }
  .art--fireworks-left  { left: 12px;  top: 12px;  width: 180px; height: 120px;
    background: linear-gradient(160deg, var(--art-spark), rgba(111,122,58,0.3)); }
  .art--balloons-left   { left: 20px;  top: 140px; width: 130px; height: 110px;
    background: linear-gradient(180deg, var(--art-balloon), rgba(142,74,54,0.35)); }
  .art--cake            { left: 110px; top: 270px; width: 160px; height: 60px;
    background: linear-gradient(180deg, var(--art-cake), rgba(154,154,154,0.35)); }
  .art--fireworks-right { left: 390px; top: 40px;  width: 120px; height: 90px;
    background: linear-gradient(160deg, var(--art-spark), rgba(111,122,58,0.3)); }
  .art--balloons-right  { left: 395px; top: 135px; width: 140px; height: 170px;
    background: linear-gradient(180deg, var(--art-balloon), rgba(142,74,54,0.35)); }

  .brand {
    position: absolute;
    left: 50%;
    transform: translateX(-50%);
    display: flex;
    align-items: center;
    gap: 10px;
    white-space: nowrap;
  }
  .brand__mark { width: 18px; height: 18px; border-radius: 50%; background: var(--brand-red); }
  .brand__name { color: var(--brand-red); font-weight: 700; font-size: 32px;
    text-shadow: 0 0 6px var(--glow), 0 0 3px var(--glow); }
  .card--front .brand { top: 140px; left: 275px; }
  .tagline {
    position: absolute; top: 196px; left: 275px; transform: translateX(-50%);
    font-size: 16px; text-align: center; line-height: 1.15; font-weight: 700; white-space: nowrap;
  }

  .services { position: absolute; list-style: none; font-size: 34px; line-height: 44px; }
  .services--left  { left: 40px;  top: 162px; }
  .services--right { right: 30px; top: 206px; text-align: right; }

  .card--back .role  { position: absolute; top: 46px; width: 100%; text-align: center; font-size: 38px; }
  .card--back .brand { top: 156px; }
  .contact { position: absolute; top: 234px; width: 100%; text-align: center; font-size: 26px; line-height: 30px; }
</style>
</head>
<body>
  <section class="card card--front" aria-label="Business card front">
    <div class="art art--fireworks-left" role="img" aria-label="Fireworks burst"></div>
    <div class="art art--balloons-left" role="img" aria-label="Party balloons"></div>
    <div class="art art--cake" role="img" aria-label="Celebration cake"></div>
    <div class="art art--fireworks-right" role="img" aria-label="Fireworks burst"></div>
    <div class="art art--balloons-right" role="img" aria-label="Party balloons"></div>

    <div class="brand"><span class="brand__mark"></span><span class="brand__name">Tov Fest Falcons</span></div>
    <p class="tagline glow-text">Delivering The Ultimate<br>Treasures To Your Party</p>

    <ul class="services services--left glow-text">
      <li>DJ's</li>
      <li>Catering</li>
      <li>All party supplies</li>
    </ul>
    <ul class="services services--right glow-text">
      <li>Tinyvolta</li>
      <li>and more...</li>
    </ul>
  </section>

  <section class="card card--back" aria-label="Business card back">
    <h1 class="role glow-text">Tov Owner &amp; Manager</h1>
    <div class="brand"><span class="brand__mark"></span><span class="brand__name">Tov Fest Falcons</span></div>
    <p class="contact glow-text">Phone : 0481927354<br>Mail : tovfestfalcons@mailbright.example</p>
  </section>
</body>
</html>
```